Pellston Ironstags Website

A revamp of the design @ pellstonfootball.com.

Colors and logos must remain same, as does the content and schedules. But we would like a new look to the whole thing.

```html
<!DOCTYPE html>
<html lang="en">
<head>
<meta charset="utf-8">
<title>Pellston Ironstags – Messages</title>
<link rel="stylesheet" href="https://fonts.googleapis.com/css2?family=Signika:wght@300;400;600&display=swap">
<style>
  :root {
    --bg-dark: #3a4541;
    --bg-mid: #46544f;
    --bg-light: #5d6e68;
    --band: #56675f;
    --band-edge: #62736c;
    --text: #e6ebe8;
    --text-soft: #cfd8d4;
    --accent: #a9dcc8;
    --field-line: #c6d0cc;
    --nav-top: #ffffff;
    --nav-bottom: #dcdedd;
    --nav-text: #3a3f3d;
    --nav-divider: #c9cbca;
    --button: #b5c3bd;
    --button-text: #2f3a36;
    --icon-bg: #e4e7e5;
    --icon-ink: #5a5f5d;
  }
  * { box-sizing: border-box; margin: 0; padding: 0; }
  html, body { width: 1200px; height: 700px; overflow: hidden; }
  body {
    position: relative;
    font-family: "Signika", sans-serif;
    color: var(--text);
    background:
      radial-gradient(ellipse 700px 500px at 0% 100%, var(--bg-light) 0%, rgba(93,110,104,0) 70%),
      linear-gradient(180deg, var(--bg-dark) 0%, var(--bg-mid) 100%);
  }
  .site-name {
    position: absolute; left: 95px; top: 46px;
    display: flex; align-items: center; gap: 14px;
    font-family: "Signika", sans-serif; font-weight: 400;
    font-size: 32px; line-height: 40px; color: var(--text-soft);
  }
  .site-name .mark {
    width: 22px; height: 22px; border-radius: 50%; background: var(--text-soft);
  }
  .main-nav {
    position: absolute; left: 505px; top: 42px; width: 600px; height: 53px;
    display: flex; border-radius: 3px;
    background: linear-gradient(180deg, var(--nav-top) 0%, var(--nav-bottom) 100%);
    box-shadow: 0 3px 6px rgba(0,0,0,0.35);
  }
  .main-nav a {
    flex: 1; display: flex; align-items: center; justify-content: center;
    font-size: 16px; font-weight: 300; color: var(--nav-text); text-decoration: none;
    border-left: 1px solid var(--nav-divider);
  }
  .main-nav a:first-child { border-left: none; }

  .messages-head {
    position: absolute; left: 90px; top: 131px; width: 1015px; height: 43px;
    background: linear-gradient(180deg, var(--band-edge), var(--band));
    font-size: 15px; font-weight: 300; color: var(--text-soft);
  }
  .messages-head span { position: absolute; top: 12px; }
  .col-date-h { left: 48px; } .col-from-h { left: 239px; } .col-msg-h { left: 403px; }

  .message-list { position: absolute; left: 90px; top: 210px; width: 1000px; font-weight: 300; font-size: 15px; color: var(--text-soft); }
  .message-row { position: relative; height: 36px; }
  .message-row span { position: absolute; top: 0; white-space: nowrap; overflow: hidden; }
  .msg-date { left: 19px; } .msg-from { left: 235px; }
  .msg-text { left: 408px; width: 585px; }

  .scrollbar { position: absolute; left: 1093px; top: 180px; }

  .divider {
    position: absolute; left: 222px; top: 409px; width: 774px; height: 2px;
    background: linear-gradient(90deg, rgba(120,140,132,0), #6f837b 30%, #6f837b 70%, rgba(120,140,132,0));
  }
  .form-heading {
    position: absolute; left: 0; width: 1262px; top: 420px; text-align: center;
    font-size: 15px; font-weight: 400; color: var(--accent);
  }
  .form-label { position: absolute; top: 458px; font-size: 16px; font-weight: 400; color: var(--accent); }
  .label-from { left: 379px; } .label-colon { left: 458px; }
  .field { position: absolute; border: 1px solid var(--field-line); background: transparent; }
  .field-from { left: 488px; top: 455px; width: 298px; height: 26px; }
  .field-body { left: 491px; top: 496px; width: 601px; height: 116px; }
  .post-button {
    position: absolute; left: 1104px; top: 568px; width: 53px; height: 39px;
    border-radius: 20px; background: var(--button); color: var(--button-text);
    font-size: 15px; font-weight: 400; display: flex; align-items: center; justify-content: center;
  }

  .footer-line { position: absolute; left: 14px; top: 623px; width: 1152px; height: 1px; background: #66766f; }
  .footer-nav a {
    position: absolute; top: 650px; transform: translateX(-50%);
    font-size: 15px; font-weight: 300; color: var(--text-soft); text-decoration: none;
  }
  .social { position: absolute; top: 643px; left: 977px; display: flex; gap: 15px; }
  .social span {
    width: 30px; height: 30px; border-radius: 4px; background: var(--icon-bg);
    display: flex; align-items: center; justify-content: center;
  }
</style>
</head>
<body>
  <div class="site-name"><span class="mark"></span>Pellston Ironstags</div>

  <nav class="main-nav">
    <a href="#">Home</a><a href="#">Pictures</a><a href="#">Messages</a><a href="#">Stats</a><a href="#">Contact us</a>
  </nav>

  <div class="messages-head">
    <span class="col-date-h">Date</span><span class="col-from-h">From</span><span class="col-msg-h">Message</span>
  </div>

  <div class="message-list">
    <div class="message-row"><span class="msg-date">2011-10-04 06:42:47</span><span class="msg-from">Morgan</span><span class="msg-text">This is a test</span></div>
    <div class="message-row"><span class="msg-date">2009-08-24 05:18:24</span><span class="msg-from">Morgan</span><span class="msg-text">We never heard from anyone about fall baseball so Evan ended up</span></div>
    <div class="message-row"><span class="msg-date">2009-07-22 05:46:17</span><span class="msg-from">Morgan</span><span class="msg-text">Evan R. has decided to play fall baseball instead of football this year. ticipating too!</span></div>
    <div class="message-row"><span class="msg-date">2009-07-01 09:05:59</span><span class="msg-from">Morgan</span><span class="msg-text">Any thoughts yet on fall ball?</span></div>
  </div>

  <svg class="scrollbar" width="12" height="240" viewBox="0 0 12 240" aria-hidden="true">
    <rect x="0" y="0" width="12" height="240" rx="5" fill="#ffffff"/>
    <path d="M3 9 L6 4 L9 9 Z" fill="#333"/>
    <path d="M3 231 L6 236 L9 231 Z" fill="#333"/>
    <rect x="3" y="25" width="6" height="109" rx="1" fill="#3c4542"/>
  </svg>

  <div class="divider"></div>
  <div class="form-heading">Add a new message below:</div>
  <div class="form-label label-from">From</div>
  <div class="form-label label-colon">:</div>
  <div class="field field-from"></div>
  <div class="field field-body"></div>
  <div class="post-button">Post</div>

  <div class="footer-line"></div>
  <nav class="footer-nav">
    <a href="#" style="left:280px">Home</a>
    <a href="#" style="left:404px">Pictures</a>
    <a href="#" style="left:523px">Messages</a>
    <a href="#" style="left:638px">Stats</a>
    <a href="#" style="left:763px">Contact us</a>
  </nav>

  <div class="social">
    <span aria-label="Social link"></span>
    <span aria-label="Social link"></span>
    <span aria-label="Social link"></span>
    <span aria-label="Email">
      <svg width="20" height="14" viewBox="0 0 20 14" aria-hidden="true">
        <rect x="1" y="1" width="18" height="12" fill="none" stroke="var(--icon-ink)" stroke-width="2"/>
        <path d="M1 1 L10 8 L19 1" fill="none" stroke="var(--icon-ink)" stroke-width="2"/>
      </svg>
    </span>
  </div>
</body>
</html>
```